Book cover needed for Christian Non-Fiction Book

I need book cover design (eBook , Paperback, and possibly case laminate Hardcover) for use on PQL and Halvet Print.
Title: Go Forth Called
Sub-Title: Leaving Shelter and Walking in Faithful Purpose
Author: Owen Callery
Also on front cover "Forward by R. Lisel Marrow"

I like clean/simple designs. Below are links to examples of covers I like...
https://www.bookvantle.example/dp/X4821QPT7M?tag=plumwick-20&linkCode=ogi&th=1&psc=1
https://www.bookvantle.example/dp/X49KTRMWHZ?tag=plumwick-20&linkCode=ogi&th=1&psc=1
https://www.bookvantle.example/dp/X22HQC51NT?tag=plumwick-20&linkCode=ogi&th=1&psc=1
https://www.bookvantle.example/dp/X48F3WZPDR?tag=plumwick-20&linkCode=ogi&th=1&psc=1
https://www.bookvantle.example/dp/X4M7UVVCLE?tag=plumwick-20&linkCode=ogi&th=1&psc=1
https://www.bookvantle.example/dp/X2R9HNNKA6?tag=plumwick-20&linkCode=ogi&th=1&psc=1

The main idea for Go Forth Called is that God is a sending God and being "on the move" or journeying is central to God's character, and therefore God's people. I write about our hesitancy to "go," and how the Bible is full of stories about people "going" from Abraham to Jesus, to the disciples of Jesus.

The core biblical text is the Great Commission in Matthew 28:16-20, where Jesus sends out his followers, though some of them doubt.

This paragraph from the forward by R. Lisel Marrow captures the tone of the book well:
This book is a call amid the turmoil. Sacred scripture contains no shortage of narratives in which humans are pulled from their ordinary lives with an inciting incident whose stakes are high. These Biblical figures are lulled from complacency and comfort zones—and yet they are reluctant to serve because they question their ability and influence. Their lessons are relevant for us today: They, and we, are always called and sent with authority. The power of the Holy Spirit equips their “going”—and ours. It’s a sending out that looks less like mastery and more humility. It’s a sending out that is unequivocal service to others modelled in a rabbi-reformer who washed feet and touched the unclean.

I have previously published two shorter books and would be very interested in getting new covers for the old books these so that the three have a similar feel. Whichever designer I go with for "Go Forth Called" I would also want to work with on creating a "branded look" for the other two books.

Target Market(s)

Christian, Religion, Spirituality Readers

Requirements
Must have
• The front cover must have this copy...
Go Forth Called
Leaving Shelter and Walking in Faithful Purpose
Owen Callery
Forward by R. Lisel Marrow

Must be willing to do the full paperback and/or hardcover, but start with thefront cover please
Nice to have
• See attached files for some book covers I like

```html
<!DOCTYPE html>
<html lang="en">
<head>
<meta charset="utf-8">
<title>Go Forth Called — Front Cover</title>
<link rel="stylesheet" href="https://fonts.googleapis.com/css2?family=Josefin+Sans:wght@300;400&display=swap">
<style>
  :root {
    --paper: #f2f0eb;
    --paper-streak: rgba(200, 195, 185, 0.18);
    --title-red: #d63a1c;
    --title-red-deep: #b8260f;
    --ink: #2a2624;
    --author-brown: #6a4528;
    --gold: #d9a93a;
    --sky: #b9cfdc;
    --rim: #a9aaa8;
  }
  * { margin: 0; padding: 0; box-sizing: border-box; }
  html, body { width: 800px; height: 1200px; overflow: hidden; }
  body { background: var(--paper); }

  .cover {
    position: relative;
    width: 800px;
    height: 1200px;
    overflow: hidden;
    background:
      repeating-linear-gradient(92deg, transparent 0 3px, var(--paper-streak) 3px 4px, transparent 4px 9px),
      var(--paper);
    font-family: "Josefin Sans", "Century Gothic", sans-serif;
    text-align: center;
  }

  .cover-art {
    position: absolute;
    left: 0;
    top: 0;
    width: 520px;
    height: 620px;
  }

  .title {
    position: absolute;
    left: 0;
    right: 0;
    top: 432px;
    font-weight: 400;
    font-size: 146px;
    line-height: 160px;
    letter-spacing: 2px;
    text-transform: uppercase;
    background: linear-gradient(180deg, var(--title-red), var(--title-red-deep));
    -webkit-background-clip: text;
    background-clip: text;
    color: transparent;
  }

  .subtitle {
    position: absolute;
    left: 0;
    right: 0;
    top: 770px;
    font-weight: 400;
    font-size: 24px;
    line-height: 54px;
    letter-spacing: 2.5px;
    text-transform: uppercase;
    color: var(--ink);
  }
  .subtitle span { display: block; }

  .author {
    position: absolute;
    left: 0;
    right: 0;
    top: 1056px;
    font-weight: 400;
    font-size: 60px;
    line-height: 64px;
    letter-spacing: 2px;
    text-transform: uppercase;
    color: var(--author-brown);
  }

  .foreword {
    position: absolute;
    left: 0;
    right: 0;
    top: 1130px;
    font-weight: 400;
    font-size: 25px;
    letter-spacing: 1.5px;
    text-transform: uppercase;
    color: var(--author-brown);
  }
</style>
</head>
<body>
  <main class="cover">
    <svg class="cover-art" viewBox="0 0 520 620" role="img" aria-label="Illustration of a red and white bird diving out of a round sky window surrounded by a golden sunburst">
      <defs>
        <radialGradient id="sunburst" cx="90" cy="170" r="420" gradientUnits="userSpaceOnUse">
          <stop offset="0" stop-color="var(--gold)" stop-opacity="0.95"/>
          <stop offset="0.45" stop-color="var(--gold)" stop-opacity="0.55"/>
          <stop offset="1" stop-color="var(--gold)" stop-opacity="0"/>
        </radialGradient>
        <linearGradient id="window-sky" x1="0" y1="0" x2="0" y2="1">
          <stop offset="0" stop-color="#cfdde6"/>
          <stop offset="1" stop-color="var(--sky)"/>
        </linearGradient>
      </defs>
      <circle cx="90" cy="170" r="420" fill="url(#sunburst)"/>
      <circle cx="90" cy="150" r="110" fill="url(#window-sky)" stroke="var(--rim)" stroke-width="8"/>
    </svg>

    <h1 class="title">Go Forth<br>Called</h1>

    <p class="subtitle">
      <span>Leaving Shelter</span>
      <span>and Walking</span>
      <span>in</span>
      <span>Faithful Purpose</span>
    </p>

    <p class="author">Owen Callery</p>
    <p class="foreword">Forward by R. Lisel Marrow</p>
  </main>
</body>
</html>
```